Exceptional Corporate Business Card Design

Hello,

We need an exceptional corporate business card design based on our logo attached. We require:

1. A Variation for letterpress print
2. Standard size of business card 84mm x 55mm (Artwork 88mm x 59mm)
3. Variation for square business card 65mm x 65mm (Artwork 69mm x 69mm)
4. Variation as a one side print
5. Adobe Illustrator files

The company is in the financial industry, valmisto.com

The logo is attached as vector pdf.
regards

```html
<!DOCTYPE html>
<html lang="en">
<head>
<meta charset="utf-8">
<title>Valmisto Business Cards</title>
<link rel="stylesheet" href="https://fonts.googleapis.com/css2?family=Raleway:wght@400;500;600&display=swap">
<style>
  :root {
    --backdrop: #3b322e;
    --paper: #f7f7f5;
    --paper-edge: #e4e4e0;
    --brand-blue: #1e3a8c;
    --press-grey: #c9c9c6;
  }
  * { box-sizing: border-box; margin: 0; padding: 0; }
  html, body {
    width: 1200px;
    height: 768px;
    overflow: hidden;
    background: var(--backdrop);
    font-family: "Raleway", sans-serif;
  }
  .canvas {
    position: relative;
    width: 1200px;
    height: 768px;
  }
  .card {
    position: absolute;
    top: 214px;
    width: 520px;
    height: 340px;
    background: var(--paper);
    border: 1px solid var(--paper-edge);
  }
  .card--front { left: 50px; }
  .card--back { left: 630px; }

  /* Front: letterpress wordmark */
  .front-mark {
    position: absolute;
    left: 0; right: 0; top: 0; bottom: 0;
    display: flex;
    align-items: center;
    justify-content: center;
    gap: 18px;
  }
  .front-mark__dot {
    width: 74px;
    height: 74px;
    border-radius: 50%;
    background: var(--press-grey);
  }
  .front-mark__name {
    font-size: 62px;
    font-weight: 500;
    letter-spacing: 2px;
    color: var(--press-grey);
  }

  /* Back: contact details */
  .back-mark {
    position: absolute;
    left: 34px;
    top: 34px;
    display: flex;
    align-items: center;
    gap: 10px;
  }
  .back-mark__dot {
    width: 40px;
    height: 40px;
    border-radius: 50%;
    background: var(--brand-blue);
  }
  .back-mark__name {
    font-size: 32px;
    font-weight: 600;
    letter-spacing: 1px;
    color: var(--brand-blue);
  }
  .holder {
    position: absolute;
    left: 34px;
    top: 116px;
    color: var(--brand-blue);
  }
  .holder__name { font-size: 17px; font-weight: 400; }
  .holder__title { font-size: 9px; margin-top: 2px; }
  .contacts {
    position: absolute;
    left: 34px;
    top: 176px;
    list-style: none;
    color: var(--brand-blue);
    font-size: 11px;
    line-height: 18px;
  }
  .contacts li { display: flex; align-items: center; gap: 10px; }
  .contacts svg { width: 9px; height: 9px; fill: var(--brand-blue); }
  .address {
    position: absolute;
    left: 34px;
    top: 240px;
    font-size: 10px;
    color: var(--brand-blue);
  }
  .company {
    position: absolute;
    right: 34px;
    top: 168px;
    font-size: 17px;
    letter-spacing: 1px;
    color: var(--brand-blue);
  }
</style>
</head>
<body>
<main class="canvas">
  <section class="card card--front" aria-label="Card front">
    <div class="front-mark">
      <span class="front-mark__dot"></span>
      <span class="front-mark__name">VALMISTO</span>
    </div>
  </section>

  <section class="card card--back" aria-label="Card back">
    <div class="back-mark">
      <span class="back-mark__dot"></span>
      <span class="back-mark__name">VALMISTO</span>
    </div>

    <div class="holder">
      <p class="holder__name">Your Long Name</p>
      <p class="holder__title">Your title</p>
    </div>

    <ul class="contacts">
      <li>
        <svg viewBox="0 0 10 10" aria-hidden="true"><path d="M2 0.5 L4 2.8 L3 4 Q4.2 6 6 7 L7.2 6 L9.5 8 L8.2 9.5 Q3.5 9 0.5 1.8 Z"/></svg>
        <span>0000-000-000</span>
      </li>
      <li>
        <svg viewBox="0 0 10 10" aria-hidden="true"><path d="M0.5 2 H9.5 V8 H0.5 Z M1 2.5 L5 5.5 L9 2.5" fill="none" stroke="currentColor"/><rect x="0.5" y="2" width="9" height="6" fill="#1e3a8c"/></svg>
        <span>office@valmisto.com</span>
      </li>
      <li>
        <svg viewBox="0 0 10 10" aria-hidden="true"><circle cx="5" cy="5" r="4.5"/></svg>
        <span>www.valmisto.com</span>
      </li>
    </ul>

    <p class="address">48 Harlow Lane, EC2 7QT, London, England</p>

    <p class="company">VALMISTO PLC</p>
  </section>
</main>
</body>
</html>
```